Funky Entertainment and Music Solutions Company

Miles Darrow Entertainment (www.milesdarrow-example.com) needs a fresh new face. We are in Entertainment and Music Solutions for corporate and private functions providing a very hands-on and customer focused premium approach to our client's entertainment needs.

Current Logo:
It's the MILES DARROW ENTERTAINMENT found on our website above

What do we do?
We advise, organise, source and manage your event (big or small) from a string quartet for a cocktail party to pre-dinner entertainment and big band entertainment for the corporate Christmas Party.

Our Objective:
To become the main Entertainment and Music Solutions provider to large Australia/Asia Pac corporations as well as private parties.

Look and Feel?
We have recently released our new services booklet found here: http://www.pagetumble-example.com/3A1B2C4D5E6/q2mr814x and whilst we don't want the site to look like a rainbow, it should incorporate the sleek, funky, clean look that we're tying to achieve.

Main pages we're after:
- Welcome/About Us
- Services (ie, strings, Covers Bands, Jazz Groups. All found in above booklet)
- Enquiry/Booking Page
- Gallery and Audio Page
Updates

This project now has a committed budget - submit away!
Thanks all!
Miles Darrow Entertainment

Just a few updates on the project.
- We are trying to move away from what the current website offers. Our new client focus is corporate and private parties, not nightclubs. A great example are the images on the first and last pages of the flipbook: http://www.pagetumble-example.com/3A1B2C4D5E6/q2mr814x
- Some websites that we like are found below. They are sleek, easy to navigate and not too much scrolling required. They incorporate a cool background with the floating ttext/images in the centre.
http://velloria-sf-example.com/
http://www.quartzharbor-example.com/
- Any questions, please ask!
Thanks and happy designing! :)

Industry/Entity Type

Entertainment

```html
<!DOCTYPE html>
<html lang="en">
<head>
<meta charset="utf-8">
<title>Miles Darrow Entertainment</title>
<link rel="stylesheet" href="https://fonts.googleapis.com/css2?family=Source+Sans+3:wght@400;600;700&family=Anton&family=Courgette&family=Philosopher&display=swap">
<style>
:root{
  --bg:#000;
  --purple:#7b63d6;
  --purple-light:#8e74ee;
  --purple-deep:#6a52c4;
  --purple-shadow:#7457d8;
  --lavender:#b9a6f6;
  --ink-purple:#4a35a0;
  --label:#8b7fd0;
  --white:#fff;
  --logo:#e6e6e6;
  --frame:#2a2440;
  --dark:#151515;
}
*{margin:0;padding:0;box-sizing:border-box}
html,body{width:1200px;height:896px;overflow:hidden;background:var(--bg)}
body{position:relative;font-family:"Source Sans 3",sans-serif;color:var(--white)}
.abs{position:absolute}

.brand{left:168px;top:36px;font-weight:700;color:var(--logo);font-size:33px;line-height:29px;letter-spacing:-0.5px}
.booking{left:710px;top:20px;font-family:"Philosopher",sans-serif;font-size:16px}
.booking .label{color:var(--label)}

.nav{left:495px;top:70px;width:534px;height:51px;background:var(--purple);border-radius:4px 4px 0 0;display:flex;align-items:center;padding-left:58px;gap:8px;font-size:17px}
.nav a{color:var(--white);text-decoration:none}
.nav .sep{color:#d9d0ff;margin:0 2px}
.home{left:495px;top:66px;width:45px;height:56px;background:var(--lavender);border-radius:4px 4px 0 0;display:flex;align-items:center;justify-content:center}

.hero{left:0;top:0}
.photo{left:136px;top:131px;width:530px;height:309px;background:linear-gradient(135deg,#1b1530 0%,#3a2d66 40%,#6b4fb0 60%,#1f1a2e 100%)}
.headline{left:692px;top:210px;line-height:1}
.headline .l1{font-size:42px;font-weight:400}
.headline .l1 b{font-family:"Anton",sans-serif;font-weight:400;font-size:46px;letter-spacing:.5px}
.headline .l2{font-size:42px;margin-top:6px}
.headline .l3{font-family:"Courgette",cursive;font-size:36px;margin-top:8px}
.learn{left:688px;top:385px;width:191px;height:40px;border-radius:20px;background:var(--lavender);color:var(--ink-purple);font-weight:700;font-size:24px;display:flex;align-items:center;justify-content:center}

.panel{left:127px;top:510px;width:921px;height:316px;border-radius:8px;background:linear-gradient(180deg,var(--purple) 0%,var(--purple-deep) 100%)}
.col-head{font-size:20px;display:flex;align-items:center;gap:8px}
.col-head b{font-weight:700}
.col-head::after{content:"";position:absolute;left:28px;top:28px;width:120px;height:1px;background:linear-gradient(90deg,rgba(255,255,255,.7),rgba(255,255,255,0))}
.intro{left:152px;top:580px;width:300px;font-size:17px;line-height:20px}
.intro2{left:152px;top:654px;width:270px;font-size:15px;line-height:19px}
.services{left:152px;top:706px;width:300px;font-size:14px;line-height:27.5px}
.services span{margin-right:8px;white-space:nowrap}
.services span::before{content:"› ";color:#d6ccff}
.services u{text-decoration-color:rgba(255,255,255,.8);text-underline-offset:4px}

.video{left:463px;top:584px;width:268px;height:213px;background:var(--dark);border-radius:6px;padding:6px}
.video .screen{width:256px;height:172px;background:linear-gradient(135deg,#3d3a2c,#6c5a48 50%,#8a3a2e);border-radius:2px;position:relative}
.play{position:absolute;left:89px;top:67px;width:78px;height:45px;background:#111;border-radius:6px;display:flex;align-items:center;justify-content:center}
.controls{display:flex;align-items:center;gap:5px;margin-top:5px;height:20px;font-size:9px;color:#aaa}
.controls .btn{width:16px;height:16px;background:#2c2c2c;border-radius:2px}
.bar{width:110px;height:3px;background:#333;position:relative}
.bar::before{content:"";position:absolute;left:0;top:0;width:80px;height:3px;background:#3ab0c8}

.thumb{width:124px;height:97px;background:var(--purple-light);border-radius:8px;padding:7px;box-shadow:inset 0 0 0 1px rgba(255,255,255,.15)}
.thumb div{width:100%;height:100%;border-radius:5px}

.copy{left:126px;top:860px;font-family:Arial,sans-serif;font-size:9px}
.social{left:894px;top:849px;width:157px;height:33px;background:#1c1c1c;display:flex;align-items:center;justify-content:center;gap:7px}
.social span{width:23px;height:23px;border-radius:50%;background:#4a4a4a}
</style>
</head>
<body>

<div class="abs brand">MILES DARROW<br>ENTERTAINMENT</div>
<div class="abs booking"><span class="label">For Booking:</span> 0400 555 018</div>

<nav class="abs nav">
  <a href="#">Services</a><span class="sep">/</span>
  <a href="#">Gallery</a><span class="sep">/</span>
  <a href="#">About us</a><span class="sep">/</span>
  <a href="#">Contact us</a>
</nav>
<div class="abs home">
  <svg width="20" height="18" viewBox="0 0 20 18"><path d="M10 0 L20 9 H17 V18 H12 V12 H8 V18 H3 V9 H0 Z" fill="#fff"/></svg>
</div>

<svg class="abs hero" width="1200" height="520" viewBox="0 0 1200 520">
  <path d="M675 140 L1060 150 Q1075 152 1075 168 L1075 470 Q1075 486 1058 485 L640 460 Z" fill="var(--purple-shadow)"/>
  <rect x="126" y="122" width="560" height="333" rx="16" fill="#fff"/>
  <path d="M669 122 L1030 122 Q1049 122 1049 142 L1049 436 Q1049 455 1030 455 L612 455 Z" fill="var(--purple-light)"/>
  <path d="M669 122 L1030 122 Q1049 122 1049 142 L1049 436 Q1049 455 1030 455 L612 455 Z" fill="url(#heroShade)"/>
  <defs>
    <linearGradient id="heroShade" x1="0" y1="0" x2="0" y2="1">
      <stop offset="0" stop-color="#9a82f4" stop-opacity=".4"/>
      <stop offset="1" stop-color="#6a52c4" stop-opacity=".6"/>
    </linearGradient>
  </defs>
</svg>
<div class="abs photo" role="img" aria-label="Singer performing on stage to a cheering crowd" style="clip-path:polygon(0 0,100% 0,100% 0,89% 100%,0 100%);border-radius:10px 0 0 10px"></div>

<div class="abs headline">
  <div class="l1">If it's <b>happening</b></div>
  <div class="l2">Out there you'll</div>
  <div class="l3">find it here...</div>
</div>
<div class="abs learn">LEARN MORE</div>

<section class="abs panel"></section>

<div class="abs col-head" style="left:152px;top:535px">
  <svg width="18" height="14" viewBox="0 0 18 14"><path d="M0 0 H8 L14 7 L8 14 H0 L6 7 Z" fill="#fff"/></svg>
  <span>MILESDARROW<b>EVENTS</b></span>
</div>
<div class="abs col-head" style="left:463px;top:535px">
  <svg width="18" height="14" viewBox="0 0 18 14"><path d="M0 0 H8 L14 7 L8 14 H0 L6 7 Z" fill="#fff"/></svg>
  <span>RECENTS <b>VIDEOS</b></span>
</div>
<div class="abs col-head" style="left:744px;top:535px">
  <svg width="18" height="14" viewBox="0 0 18 14"><path d="M0 0 H8 L14 7 L8 14 H0 L6 7 Z" fill="#fff"/></svg>
  <span>RECENTS <b>EVENTS</b></span>
</div>

<p class="abs intro">Looking for any type of advertisement or promotional services? You have landed up at the right place.</p>
<p class="abs intro2">We offer a wide assortment of services which include:</p>
<div class="abs services">
  <span><u>Event management</u></span><span><u>Corporate Events</u></span><br>
  <span><u>Conference Management</u></span><br>
  <span><u>Parties and Awards</u></span><span><u>Road Shows</u></span><br>
  <span><u>Brand Promotions</u></span><span><u>Audio Visual Production</u></span>
</div>

<div class="abs video">
  <div class="screen" role="img" aria-label="Video still of a promotional event stall">
    <div class="play"><svg width="18" height="20" viewBox="0 0 18 20"><path d="M0 0 L18 10 L0 20 Z" fill="#fff"/></svg></div>
  </div>
  <div class="controls">
    <span class="btn"></span><span class="btn"></span><span class="bar"></span>
    <span style="color:#3ab0c8;letter-spacing:-1px">▮▮▮▮▮</span><span>00:25</span><span class="btn" style="width:12px;height:12px"></span>
  </div>
</div>

<div class="abs thumb" style="left:753px;top:584px"><div role="img" aria-label="Exhibition stand at a shopping centre" style="background:linear-gradient(135deg,#6f8aa8,#2d5d8a)"></div></div>
<div class="abs thumb" style="left:896px;top:584px"><div role="img" aria-label="Promotional game stall with staff" style="background:linear-gradient(135deg,#8a7a5a,#c0392b)"></div></div>
<div class="abs thumb" style="left:753px;top:700px"><div role="img" aria-label="Balloon display at a brand event" style="background:linear-gradient(135deg,#c04a7a,#e0a030)"></div></div>
<div class="abs thumb" style="left:896px;top:700px"><div role="img" aria-label="Car showcased at a mall activation" style="background:linear-gradient(135deg,#d8c8a0,#b03a2a)"></div></div>

<footer>
  <div class="abs copy">Copyright © 2013 Northlane Studio</div>
  <div class="abs social">
    <span></span><span></span><span></span><span></span>
    <svg width="23" height="23" viewBox="0 0 23 23"><circle cx="11.5" cy="11.5" r="11.5" fill="#4a4a4a"/><circle cx="10" cy="10" r="4.5" fill="none" stroke="#1c1c1c" stroke-width="2"/><path d="M13.5 13.5 L17 17" stroke="#1c1c1c" stroke-width="2.5" stroke-linecap="round"/></svg>
  </div>
</footer>

</body>
</html>
```